Spanish Student Needs a Cover for his PhD Dissertation

Hi everyone :) So, I'm a Corneal surgeon currently finishing my PhD, with a dissertation focused on the evaluation of quality of life in patients affected by a disease called Keratoconus. Just so you know, Keratoconus is a condition in which the cornea (the frontal part of the way) gets thin and bulgy and it decreases vision. What I did during my PhD was designing a questionnaire for evaluating quality of life in this kind of patients.
I need to design a hard cover for my dissertation, which is 200 sheets long. I like kind of minimalistic and geometric designs but I am totally open to suggestions. What needs to be in the cover is the name of the dissertation "Diseño, desarrollo y validación de una encuesta para evaluar el compromiso visual y emocional subjetivos en pacientes con Queratocono" and my name, "Iñigo Tarrasco". The other thing that needs to go there is the logo of my university (Universidad de Montebrisa). Aside from that, anything else is up to the designer. It would be important to use the kind of "red" color I am using in the dissertation. I am attaching the frontal page of my dissertation so you know what kind of design and colors I am using.
In the back part, of the cover, there should be this small inscription: "Iñigo Tarrasco, MD, es un Oftalmólogo Subespecialista en Cirugía Refractiva de la Universidad Serrana Metropolitana (Colombia) y la Universidad de Montebrisa (España). Actualmente se desempeña como miembro del Departamento de Córnea y Cirugía Refractiva de la Clínica de Oftalmología Vallealto y como director de su propia compañía de emprendimiento médico Silver Heron Surgical". Please leave a space to place my picture; I will have it taken this week so I don't have it right now, you can just leave the blank spot and I will include it later
The size of the pages is standard "letter" size.
Thanks a lot!

Target Market(s)

PhD Scholars

Font styles to use
Serif

Requirements
Must have
• The "red" color I use on my font. It must be formal but "young".
Nice to have
• I like to keep the design clean, kind of "formal with a young" touch so to speak. I really like gray colors, so it would be nice to have broad areas of gray. I love geometrical designs.
I have uploaded a very early version a friend of mine made (it even had a different title); this can be a starting point for you to work on, but I am more than open to suggestions and new ideas.
Should not have
• Please don't use my whole name, Iñigo Tarrasco is fine. I don't like ALL CAPITALS.

```html
<!DOCTYPE html>
<html lang="es">
<head>
<meta charset="utf-8">
<title>Cubierta de tesis doctoral – Iñigo Tarrasco</title>
<link rel="stylesheet" href="https://fonts.googleapis.com/css2?family=Crimson+Pro:wght@400&family=Lexend:wght@600&family=Noto+Serif:wght@700&family=Roboto:wght@700&display=swap">
<style>
  :root {
    --crimson: #ad1e42;
    --crimson-bright: #d8204c;
    --charcoal: #252525;
    --paper: #ffffff;
    --white: #ffffff;
  }
  * { margin: 0; padding: 0; box-sizing: border-box; }
  html, body {
    width: 1200px; height: 930px; overflow: hidden;
    background: var(--paper);
  }
  .sheet { position: relative; width: 1200px; height: 930px; }

  .side-label {
    position: absolute;
    font-family: "Crimson Pro", serif;
    font-size: 22px;
    color: var(--crimson);
    transform: translateX(-50%);
  }
  .side-label--front { left: 316px; top: 52px; }
  .side-label--back  { left: 890px; top: 59px; }

  .cover {
    position: absolute;
    top: 112px;
    height: 680px;
    box-shadow: 6px 8px 10px rgba(0,0,0,.45);
    overflow: hidden;
  }
  .cover--front { left: 53px; width: 526px; background: var(--crimson); }
  .cover--back  { left: 602px; width: 528px; height: 681px; background: var(--charcoal); }

  .cover__art { position: absolute; inset: 0; width: 100%; height: 100%; display: block; }

  /* front: university block */
  .crest {
    position: absolute; left: 59px; top: 17px;
    width: 52px; height: 52px; border-radius: 50%;
    background: var(--white);
  }
  .crest-rule {
    position: absolute; left: 21px; top: 75px; width: 128px; height: 1px;
    background: rgba(255,255,255,.7);
  }
  .university-name {
    position: absolute; left: 0; top: 84px; width: 170px;
    text-align: center;
    font-family: "Roboto", sans-serif; font-weight: 700;
    font-size: 10.5px; color: var(--white);
  }
  .school-badge {
    position: absolute; left: 24px; top: 102px; width: 123px; height: 31px;
    background: var(--white);
    display: flex; align-items: center; justify-content: center; gap: 6px;
  }
  .school-badge__mark { width: 9px; height: 9px; background: var(--crimson); }
  .school-badge__name {
    font-family: "Roboto", sans-serif; font-weight: 700;
    font-size: 15px; color: var(--charcoal); letter-spacing: .5px;
  }

  /* front: title */
  .thesis-title {
    position: absolute; right: 16px; top: 144px; width: 340px;
    text-align: right;
    font-family: "Noto Serif", serif; font-weight: 700;
    font-size: 22.5px; line-height: 29px; letter-spacing: .6px;
    color: var(--white);
  }
  .institution {
    position: absolute; right: 14px; top: 339px;
    font-family: "Lexend", sans-serif; font-weight: 600;
    font-size: 17.5px; letter-spacing: .4px;
    color: var(--crimson-bright);
  }
  .author {
    position: absolute; left: 263px; top: 620px;
    transform: translateX(-50%);
    white-space: nowrap;
    font-family: "Lexend", sans-serif; font-weight: 600;
    font-size: 22px; letter-spacing: 1.5px;
    color: var(--white);
  }

  /* back */
  .back-band {
    position: absolute; left: 95px; top: 0; width: 335px; height: 100%;
    background: var(--crimson);
  }
  .author-bio {
    position: absolute; left: 105px; top: 39px; width: 315px;
    text-align: center;
    font-family: "Crimson Pro", serif;
    font-size: 16.2px; line-height: 18.6px;
    color: var(--white);
  }
  .photo-slot {
    position: absolute; left: 95px; top: 407px; width: 335px;
    text-align: center;
    font-family: "Crimson Pro", serif;
    font-size: 16.5px; color: var(--white);
  }
</style>
</head>
<body>
<main class="sheet">
  <span class="side-label side-label--front">Front</span>
  <span class="side-label side-label--back">Back</span>

  <section class="cover cover--front">
    <svg class="cover__art" viewBox="0 0 962 1244" preserveAspectRatio="none" aria-hidden="false">
      <defs>
        <linearGradient id="eye-tones" x1="0" y1="0" x2="1" y2="1">
          <stop offset="0" stop-color="#3a2a26"/>
          <stop offset="0.35" stop-color="#b4562f"/>
          <stop offset="0.6" stop-color="#8f7a3a"/>
          <stop offset="1" stop-color="#e9d6d6"/>
        </linearGradient>
        <filter id="edge-shadow" x="-10%" y="-10%" width="120%" height="120%">
          <feGaussianBlur stdDeviation="6"/>
        </filter>
      </defs>
      <!-- charcoal field -->
      <polygon fill="var(--charcoal)" points="961,0 78,366 0,310 0,1244 961,1244"/>
      <!-- photo area -->
      <polygon role="img" aria-label="Close-up photograph of a human eye with lashes and an amber-green iris"
               fill="url(#eye-tones)" points="0,400 610,925 0,1175"/>
      <!-- band shadows -->
      <line x1="78" y1="377" x2="961" y2="1136" stroke="rgba(0,0,0,.55)" stroke-width="8" filter="url(#edge-shadow)"/>
      <!-- right crimson stripe -->
      <polygon fill="var(--crimson)" points="961,781 683,891 961,1136 961,1084 755,907 961,826"/>
      <!-- bottom crimson field -->
      <polygon fill="var(--crimson)" points="0,1175 610,925 961,1226 961,1244 0,1244"/>
      <!-- title rules -->
      <rect x="561" y="251" width="401" height="5" fill="var(--crimson)"/>
      <rect x="561" y="594" width="401" height="5" fill="var(--crimson)"/>
    </svg>

    <span class="crest" role="img" aria-label="Escudo universitario"></span>
    <span class="crest-rule"></span>
    <p class="university-name">Universidad de Montebrisa</p>
    <div class="school-badge">
      <span class="school-badge__mark"></span>
      <span class="school-badge__name">EDUM</span>
    </div>

    <h1 class="thesis-title">"Diseño, desarrollo y<br>validación de una encuesta<br>para evaluar el compromiso<br>visual y emocional<br>subjetivos en pacientes con<br>Queratocono"</h1>
    <p class="institution">Universidad de Montebrisa</p>
    <p class="author">Iñigo Tarrasco</p>
  </section>

  <section class="cover cover--back">
    <div class="back-band"></div>
    <p class="author-bio">"Iñigo Tarrasco, MD, es un Oftalmólogo Subespecialista en Cirugía Refractiva de la Universidad Serrana Metropolitana (Colombia) y la Universidad de Montebrisa (España). Actualmente se desempeña como miembro del Departamento de Córnea y Cirugía Refractiva de la Clínica de Oftalmología Vallealto y como director de su propia compañía de emprendimiento médico Silver Heron Surgical"</p>
    <p class="photo-slot">Author Photo here</p>
  </section>
</main>
</body>
</html>
```